Harbor Kindness Fund - New Website Design

I need a site that looks like this http://wheelgift-relief.org for boat donations. So please replace the cars with boats.

```html
<!DOCTYPE html>
<html lang="en">
<head>
<meta charset="utf-8">
<title>Harbor Kindness Fund – Donate Boats to Charity</title>
<link href="https://fonts.googleapis.com/css2?family=Montserrat:wght@400;500;600;700&family=Quicksand:wght@400;500;600;700&display=swap" rel="stylesheet">
<style>
:root{
  --navy:#16233f;
  --coral:#e07659;
  --coral-dark:#c9523b;
  --red:#e0261f;
  --rust:#c9492b;
  --hero-bg:#e8d6cc;
  --field:#eef0f4;
  --grey-shape:#e3e3e3;
  --ink:#2d2d2d;
  --muted:#555;
  --faq-bg:#f6d8d3;
  --faq-item:#f4ecea;
  --footer:#5a5050;
  --white:#fff;
}
*{margin:0;padding:0;box-sizing:border-box}
html,body{width:705px;height:1200px;overflow:hidden;background:var(--white)}
body{position:relative;font-family:'Quicksand',sans-serif;color:var(--ink)}
.abs{position:absolute}

/* header */
.brand{left:40px;top:22px;font-family:'Montserrat',sans-serif;font-weight:700;font-size:15px;color:var(--coral);display:flex;align-items:center;gap:6px}
.brand-dot{width:12px;height:12px;border-radius:50%;background:var(--navy)}
.hotline{left:522px;top:15px;display:flex;align-items:center;gap:7px}
.hotline-tag{font-family:'Montserrat',sans-serif;font-size:7.5px;font-weight:600;color:var(--coral)}
.hotline-num{font-family:'Montserrat',sans-serif;font-size:15px;color:var(--navy);line-height:1.1}

/* nav */
.main-nav{left:12px;top:72px;width:680px;height:32px;background:var(--navy)}
.main-nav a{position:absolute;top:11px;color:var(--white);text-decoration:none;font-family:'Montserrat',sans-serif;font-weight:700;font-size:8.5px;letter-spacing:.8px}

/* hero */
.hero{left:12px;top:104px;width:680px;height:234px;background:var(--hero-bg)}
.hero-photo{left:0;top:0;width:300px;height:234px;background:linear-gradient(90deg,#e9c6ad 0%,#ecd0bd 60%,rgba(232,214,204,0) 100%)}
.hero-title{right:263px;top:108px;font-family:'Montserrat',sans-serif;font-weight:700;font-size:13px;color:#111;white-space:nowrap}
.hero-title em{font-style:normal;color:var(--red);font-size:18px}
.hero-sub{right:263px;top:132px;font-family:'Montserrat',sans-serif;font-weight:600;font-size:8px;letter-spacing:.6px;color:#222}

/* form */
.pickup-form{left:468px;top:62px;width:200px;height:256px;background:var(--coral)}
.form-notch{left:456px;top:62px}
.form-title{left:0;top:18px;width:200px;text-align:center;color:var(--white);font-family:'Montserrat',sans-serif;font-weight:600;font-size:12.5px}
.form-rule{left:58px;top:40px;width:84px;height:1px;background:var(--coral-dark)}
.field{position:absolute;height:21px;background:var(--field);font-size:8px;color:#555;padding:6px 7px 0;font-family:'Quicksand',sans-serif;font-weight:500}
.field.select::after{content:"";position:absolute;right:8px;top:9px;border-left:2.5px solid transparent;border-right:2.5px solid transparent;border-top:3.5px solid #555}
.form-sub{left:10px;top:152px;color:var(--white);font-family:'Montserrat',sans-serif;font-weight:600;font-size:9.5px}
.submit-btn{left:518px;top:301px;width:100px;height:27px;background:var(--coral-dark);color:var(--white);border-radius:3px;text-align:center;padding-top:8px;font-family:'Montserrat',sans-serif;font-weight:600;font-size:8.5px}

/* sections */
.section-title{left:0;width:705px;text-align:center;font-family:'Montserrat',sans-serif;font-weight:700;font-size:14px;letter-spacing:.8px;color:var(--navy)}
.section-title span{color:var(--rust)}
.about-text{left:38px;top:405px;width:630px;text-align:center;font-size:8.6px;line-height:16.5px;color:#444}
.donate-sub{left:0;top:511px;width:705px;text-align:center;font-size:9px;color:#666}

.perks{left:0;top:570px}
.perk-label{position:absolute;width:130px;text-align:center;font-family:'Montserrat',sans-serif;font-weight:600;font-size:8px;line-height:9.5px;color:#333}
.perk-label.light{color:var(--white)}

/* faq */
.faq{left:0;top:852px;width:705px;height:290px;background:var(--faq-bg)}
.faq-title{left:0;top:24px;width:705px;text-align:center;font-family:'Montserrat',sans-serif;font-weight:500;font-size:13.5px;color:#333}
.faq-item{position:absolute;width:306px;height:23px;background:var(--faq-item);border-radius:3px;font-family:'Montserrat',sans-serif;font-size:8.3px;color:#333;padding:7px 0 0 18px}
.faq-item::after{content:"";position:absolute;right:13px;top:6px;width:9px;height:9px;border:1px solid #999;border-radius:1px;background:linear-gradient(#999,#999) no-repeat}
.faq-item .chev{position:absolute;right:15.5px;top:9.5px;border-left:2.5px solid transparent;border-right:2.5px solid transparent;border-top:3px solid #999}
.faq-item.open{height:80px;color:var(--rust);border-radius:5px}
.faq-item.open .chev{border-top:none;border-bottom:3px solid var(--rust)}
.faq-item.open::after{border-color:var(--rust)}
.faq-item::after{background:none}
.faq-answer{margin-top:13px;width:270px;font-family:'Quicksand',sans-serif;font-size:7.6px;line-height:12.5px;color:#555}

/* footer */
.site-footer{left:0;top:1142px;width:705px;height:58px;background:var(--footer)}
.site-footer a{position:absolute;top:20px;color:var(--white);text-decoration:none;font-family:'Montserrat',sans-serif;font-weight:500;font-size:8.5px}
.copyright{left:0;top:40px;width:705px;text-align:center;font-size:7.5px;color:#ddd}
</style>
</head>
<body>

<header>
  <div class="abs brand"><span class="brand-dot"></span>Harbor Kindness Fund</div>
  <div class="abs hotline">
    <svg width="30" height="28" viewBox="0 0 30 28" aria-hidden="true">
      <circle cx="18" cy="13" r="10" fill="none" stroke="#333" stroke-width="2"/>
      <text x="18" y="17" text-anchor="middle" font-family="Montserrat,sans-serif" font-weight="700" font-size="10" fill="#333">24</text>
      <path d="M3 6c-2 5 1 13 9 18l3-3-3-3-2 1c-2-2-3-4-4-7l2-1-1-4z" fill="#333"/>
    </svg>
    <div>
      <div class="hotline-tag">It's Easy And Free</div>
      <div class="hotline-num">1-800-555-0142</div>
    </div>
  </div>
</header>

<nav class="abs main-nav">
  <a href="#" style="left:28px">HOME</a>
  <a href="#" style="left:89px">ABOUT US</a>
  <a href="#" style="left:175px">GET STARTED</a>
  <a href="#" style="left:275px">CONTACT US</a>
</nav>

<section class="abs hero">
  <div class="abs hero-photo" role="img" aria-label="Photo of a young girl embracing her mother, who wears a headscarf"></div>
  <div class="abs hero-title">Donate <em>Boats</em> to <em>Charity !</em></div>
  <div class="abs hero-sub">Your car can make a difference &nbsp;!</div>
</section>

<svg class="abs form-notch" width="14" height="30" viewBox="0 0 14 30" aria-hidden="true"><path d="M12 0L0 11l12 11z" fill="var(--coral)"/></svg>
<form class="abs pickup-form">
  <div class="abs form-title">Donation Pick Up Form</div>
  <div class="abs form-rule"></div>
  <div class="field" style="left:8px;top:62px;width:89px">First Name</div>
  <div class="field" style="left:103px;top:62px;width:89px">Last Name</div>
  <div class="field" style="left:8px;top:88px;width:89px">Zip Code</div>
  <div class="field" style="left:103px;top:88px;width:89px">Phone Number</div>
  <div class="field" style="left:8px;top:116px;width:184px">Email Id</div>
  <div class="abs form-sub">Auto Donation Information</div>
  <div class="field select" style="left:8px;top:176px;width:89px">Choose Year</div>
  <div class="field select" style="left:103px;top:176px;width:89px">Choose Make</div>
  <div class="field" style="left:8px;top:203px;width:184px">Model of vehicle</div>
</form>
<div class="abs submit-btn">Submit Application</div>

<section>
  <h2 class="abs section-title" style="top:358px"><span>ABOUT</span> US</h2>
  <p class="abs about-text">Harbor Kindness Fund believes that every child, no matter his or her health, deserves a chance to have a happy and fulfilling childhood. By donating your vehicle, we are able to raise funds throughout the country and help grant wishes to children with life-threatening medical conditions. A wish is an opportunity for a child to focus on something other than their medical routines, and be a kid again.</p>
</section>

<section>
  <h2 class="abs section-title" style="top:493px">DONATE <span>BOATS</span> TO <span>CHARITY</span>!</h2>
  <div class="abs donate-sub">Your car can make a difference!</div>

  <svg class="abs perks" width="705" height="225" viewBox="0 570 705 225" aria-hidden="true">
    <g fill="var(--grey-shape)">
      <path d="M84 578h76l25 58-63 62-63-62z"/>
      <path d="M249 578h76l25 58-63 62-63-62z"/>
      <path d="M411 578h76l25 58-63 62-63-62z"/>
      <path d="M566 578h76l25 58-63 62-63-62z"/>
      <path d="M370 666l63 56-22 64h-84l-20-64z" transform="rotate(3 370 725)"/>
    </g>
    <path d="M203 664l63 58-24 64h-78l-24-64z" fill="var(--coral)"/>
    <g fill="#666">
      <!-- truck -->
      <rect x="118" y="605" width="18" height="10" rx="1"/><path d="M111 597l9 8h-3l-8-7z"/>
      <circle cx="121" cy="617" r="3"/><circle cx="132" cy="617" r="3"/>
      <!-- heart -->
      <path d="M287 622c-11-8-15-13-15-18 0-5 4-8 8-8 3 0 5 2 7 4 2-2 4-4 7-4 4 0 8 3 8 8 0 5-4 10-15 18z"/>
      <!-- boat -->
      <path d="M422 596l6 5h42l6-5-10 15h-34z"/><path d="M449 590l8 11h-16z"/>
      <!-- gift -->
      <rect x="600" y="597" width="14" height="10"/><rect x="598" y="594" width="18" height="4"/>
      <path d="M588 612c6-3 12-2 18 0h10l-4 5h-20z"/>
      <!-- auction -->
      <circle cx="369" cy="709" r="11" fill="none" stroke="#666" stroke-width="2.5"/>
      <path d="M362 711l7-7 4 4-7 7z"/>
    </g>
    <g fill="var(--white)">
      <text x="200" y="720" text-anchor="middle" font-family="Montserrat,sans-serif" font-weight="700" font-size="24">$</text>
      <path d="M186 723l26-17 2 3-26 17z"/>
    </g>
  </svg>
  <div class="perk-label" style="left:57px;top:634px">Free Towing In<br>24-48 Hours</div>
  <div class="perk-label" style="left:222px;top:634px">Boat Donations Help<br>Fund Charitable<br>Programs</div>
  <div class="perk-label" style="left:384px;top:634px">We Accept<br>All Boats</div>
  <div class="perk-label" style="left:539px;top:632px">Hassle<br>Free Donation</div>
  <div class="perk-label light" style="left:137px;top:736px">Income<br>Tax Deduction</div>
  <div class="perk-label" style="left:308px;top:736px">Boat Will Be<br>Soldon the Largest<br>Auction Network</div>
</section>

<section class="abs faq">
  <h2 class="abs faq-title">Frequently Asked Questions</h2>
  <div class="faq-item" style="left:39px;top:72px">What type of vehicles can be donated ?<span class="chev"></span></div>
  <div class="faq-item" style="left:39px;top:104px">What paperwork do I need to donate my vehicle ?<span class="chev"></span></div>
  <div class="faq-item" style="left:39px;top:139px">Is my donated vehicle tax-deductible ?<span class="chev"></span></div>
  <div class="faq-item open" style="left:39px;top:176px">When will I receive my tax receipt ?<span class="chev"></span>
    <p class="faq-answer">Processing your vehicle usually takes around 4 weeks but in some cases may take longer due to particular state title requirements or title laws.</p>
  </div>
  <div class="faq-item" style="left:361px;top:72px">What if the vehicle is not registered in my name ?<span class="chev"></span></div>
  <div class="faq-item" style="left:361px;top:105px">How much will I receive as a tax deduction for my vehicle ?<span class="chev"></span></div>
  <div class="faq-item" style="left:361px;top:139px">How do I schedule a pick up ?<span class="chev"></span></div>
</section>

<footer class="abs site-footer">
  <a href="#" style="left:239px">HOME</a>
  <a href="#" style="left:295px">ABOUT US</a>
  <a href="#" style="left:366px">GET STARTED</a>
  <a href="#" style="left:447px">CONTACT US</a>
  <div class="abs copyright">Copyright 2017 &nbsp;All Rights Reserved.</div>
</footer>

</body>
</html>
```